Private Medical Clinic needs a letterhead design

Letterhead that can be edited. Letter head is needed for printing official doctor's notes, referrals, etc in a medical clinic. The letterhead should use the attached logos

```html
<!DOCTYPE html>
<html lang="en">
<head>
<meta charset="utf-8">
<title>Tall Pines Family Medicine – Letterhead</title>
<link href="https://fonts.googleapis.com/css2?family=EB+Garamond:wght@400&display=swap" rel="stylesheet">
<style>
  :root {
    --paper: #ffffff;
    --band-light: #5a6650;
    --band-dark: #374130;
    --rule-white: #ffffff;
    --faint-grey: #e1e2e0;
    --art-fill: #f3f4f2;
    --art-edge: #e8e9e7;
    --logo-white: #ffffff;
  }
  * { margin: 0; padding: 0; box-sizing: border-box; }
  html, body {
    width: 849px;
    height: 1200px;
    overflow: hidden;
    background: var(--paper);
  }
  .letterhead {
    position: relative;
    width: 849px;
    height: 1200px;
    background: var(--paper);
    font-family: "EB Garamond", Georgia, serif;
  }
  .header-band {
    position: absolute;
    top: 0;
    left: 0;
    width: 849px;
    height: 140px;
  }
  .header-logo {
    position: absolute;
    top: 56px;
    left: 96px;
    color: var(--logo-white);
    line-height: 1;
  }
  .header-logo .name {
    display: block;
    font-size: 31px;
    letter-spacing: 0.2px;
  }
  .header-logo .tagline {
    display: block;
    margin-top: 5px;
    margin-left: 2px;
    font-size: 7.5px;
    letter-spacing: 1.2px;
  }
  .background-art {
    position: absolute;
    left: 0;
    top: 480px;
    width: 849px;
    height: 720px;
  }
  .footer-mark {
    position: absolute;
    left: 428px;
    top: 1040px;
    color: var(--faint-grey);
    line-height: 1;
  }
  .footer-mark .name {
    display: block;
    font-size: 68px;
  }
  .footer-mark .tagline {
    display: block;
    margin-top: 14px;
    margin-left: 4px;
    font-size: 15px;
    letter-spacing: 3px;
  }
</style>
</head>
<body>
<main class="letterhead">
  <svg class="header-band" viewBox="0 0 849 140" xmlns="http://www.w3.org/2000/svg" aria-hidden="true">
    <defs>
      <radialGradient id="tab-shadow" cx="50%" cy="50%" r="50%">
        <stop offset="0%" stop-color="#5a6650" stop-opacity="0.55"/>
        <stop offset="100%" stop-color="#5a6650" stop-opacity="0"/>
      </radialGradient>
    </defs>
    <ellipse cx="175" cy="115" rx="85" ry="16" fill="url(#tab-shadow)"/>
    <rect x="0" y="40" width="45" height="79" fill="var(--band-light)"/>
    <rect x="0" y="68" width="35" height="51" fill="var(--band-dark)"/>
    <polygon points="46,40 57,33 57,112 46,119" fill="var(--band-dark)" stroke="var(--rule-white)" stroke-width="1.5"/>
    <polygon points="287,33 298,40 298,119 287,112" fill="var(--band-dark)" stroke="var(--rule-white)" stroke-width="1.5"/>
    <rect x="59" y="32" width="226" height="80" fill="var(--band-dark)"/>
    <rect x="300" y="40" width="549" height="79" fill="var(--band-light)"/>
    <polygon points="312,58 849,42 849,101 312,117" fill="var(--band-dark)"/>
  </svg>

  <div class="header-logo">
    <span class="name">Tall Pines</span>
    <span class="tagline">FAMILY MEDICINE</span>
  </div>

  <svg class="background-art" viewBox="0 480 849 720" xmlns="http://www.w3.org/2000/svg" role="img" aria-label="Faint grey dandelion seed head at lower left with seeds drifting up to the right">
    <circle class="seed-head-area" cx="120" cy="860" r="320" fill="var(--art-fill)" stroke="var(--art-edge)" stroke-width="1.5"/>
    <ellipse class="drifting-seeds-area" cx="650" cy="680" rx="230" ry="120" transform="rotate(-22 650 680)" fill="var(--art-fill)" stroke="var(--art-edge)" stroke-width="1.5"/>
  </svg>

  <div class="footer-mark">
    <span class="name">Tall Pines</span>
    <span class="tagline">FAMILY MEDICINE</span>
  </div>
</main>
</body>
</html>
```